Description of Adventure Certificate:
We require a certificate, that will be awarded to winners of competitions and offered to fundraising organisations for a $ value or type of event service we provide.
The certificate will be professionally printed on thick high-quality paper.
Design concept: Adventurous outer border, and exciting theme.
Title: Adventure Certificate (adventurous font)
Content: "Bringing the Thrill of Adventure to you"
Awarded To:..........................................
From:....................................................
Amount / Event: ...................................
Redemption Location:...........................
Expires:.................................................
Events listed near the base of certificate: Community events, Sports celebrations, Team building, School activities, Festivals, Vacation Care, EXPO's, Trade Shows.
Contact: M: 0418 627 349
E: info@tidalkite.com.au
Images: Tidal Kite Logo
Adventure Certificate image
Carabiner

```html
<!DOCTYPE html>
<html lang="en">
<head>
<meta charset="utf-8">
<title>Tidal Kite Adventure Certificate</title>
<link href="https://fonts.googleapis.com/css2?family=Bangers&family=Lato:wght@700&display=swap" rel="stylesheet">
<style>
  :root {
    --backdrop: #3a3a3c;
    --paper: #f3f5f7;
    --red-light: #b8302a;
    --red-mid: #9a2420;
    --red-dark: #6e1410;
    --photo-top: #8a3a34;
    --photo-bottom: #5c1512;
    --strip: #c98a78;
    --ink-white: #ffffff;
    --logo-black: #0b0b0b;
    --accent-red: #c4262a;
    --gear-light: #d9404a;
    --gear-dark: #9c1a22;
    --seal-light: #d8323a;
    --seal-dark: #a3141c;
  }
  * { margin: 0; padding: 0; box-sizing: border-box; }
  html, body { width: 1200px; height: 876px; overflow: hidden; }
  body { background: var(--backdrop); position: relative; font-family: "Lato", Arial, sans-serif; }
  .certificate {
    position: absolute; left: 99px; top: 84px; width: 1002px; height: 708px;
    background: var(--paper); overflow: hidden;
  }
  .certificate__art { position: absolute; inset: 0; width: 100%; height: 100%; }
  .title { position: absolute; font-family: "Bangers", Impact, sans-serif; font-weight: 400; color: var(--ink-white);
    text-shadow: 2px 3px 4px rgba(0,0,0,.35); white-space: nowrap; line-height: 1; }
  .title--main { left: 228px; top: 150px; font-size: 100px; letter-spacing: 3px;
    transform: rotate(-7deg) scaleX(1.32); transform-origin: left bottom; }
  .title--sub { left: 352px; top: 230px; font-size: 50px; letter-spacing: 2px;
    transform: scaleX(1.2); transform-origin: left center; }
  .field { position: absolute; display: flex; align-items: flex-end; color: var(--ink-white);
    font-size: 21px; font-weight: 700; height: 26px; white-space: nowrap; }
  .field__line { flex: 1; border-bottom: 2px solid var(--ink-white); margin-left: 6px; margin-bottom: 4px; }
  .field--awarded { left: 106px; top: 317px; width: 791px; }
  .field--from { left: 106px; top: 376px; width: 332px; }
  .field--amount { left: 444px; top: 376px; width: 453px; }
  .field--location { left: 106px; top: 434px; width: 791px; }
  .field--expires { left: 106px; top: 493px; width: 791px; }
  .brand { position: absolute; left: 78px; top: 600px; display: flex; align-items: center; gap: 12px;
    color: var(--ink-white); font-size: 34px; font-weight: 700; }
  .brand__dot { width: 34px; height: 34px; border-radius: 50%; background: var(--accent-red); }
</style>
</head>
<body>
  <main class="certificate">
    <svg class="certificate__art" viewBox="0 0 1002 708">
      <defs>
        <linearGradient id="band" x1="0" x2="1" y1="0" y2="0">
          <stop offset="0" stop-color="var(--red-light)"/>
          <stop offset="0.5" stop-color="var(--red-mid)"/>
          <stop offset="1" stop-color="var(--red-dark)"/>
        </linearGradient>
        <linearGradient id="photo" x1="0" x2="0" y1="0" y2="1">
          <stop offset="0" stop-color="var(--photo-top)"/>
          <stop offset="1" stop-color="var(--photo-bottom)"/>
        </linearGradient>
        <linearGradient id="gear" x1="0" x2="1" y1="0" y2="1">
          <stop offset="0" stop-color="var(--gear-light)"/>
          <stop offset="1" stop-color="var(--gear-dark)"/>
        </linearGradient>
        <radialGradient id="seal" cx="0.45" cy="0.4" r="0.6">
          <stop offset="0" stop-color="var(--seal-light)"/>
          <stop offset="1" stop-color="var(--seal-dark)"/>
        </radialGradient>
      </defs>
      <polygon points="185,0 213,0 701,708 670,708" fill="var(--strip)" opacity="0.9"/>
      <polygon class="photo-area" points="0,0 185,0 670,708 0,708" fill="url(#photo)" role="img" aria-label="Photo of a child climbing a tall rock climbing wall against a cloudy sky"/>
      <rect class="title-band" x="0" y="80" width="1002" height="548" fill="url(#band)" opacity="0.88"/>
      <polygon class="brand-plate" points="0,561 357,561 325,684 0,684" fill="var(--logo-black)"/>
      <rect class="carabiner-area" x="785" y="38" width="186" height="268" rx="60" fill="url(#gear)" opacity="0.85" role="img" aria-label="Photo of a red screwgate climbing carabiner"/>
      <circle class="seal-area" cx="845" cy="610" r="76" fill="url(#seal)" role="img" aria-label="Red wax seal"/>
    </svg>

    <h1 class="title title--main">ADVENTURE</h1>
    <h2 class="title title--sub">CERTIFICATE</h2>

    <div class="field field--awarded">Awarded To:<span class="field__line"></span></div>
    <div class="field field--from">From:<span class="field__line"></span></div>
    <div class="field field--amount">Amount / Event:<span class="field__line"></span></div>
    <div class="field field--location">Redemption Location:<span class="field__line"></span></div>
    <div class="field field--expires">Expires:<span class="field__line"></span></div>

    <div class="brand"><span class="brand__name">Tidal Kite</span><span class="brand__dot"></span></div>
  </main>
</body>
</html>
```